New webpage for Facility Management Company (cleaning services)

We need a new web page design for a company based in Stockholm, Sweden, called TKR Clean AB (established 1991). We provide cleaning services to the public sector, to businesses, and to home owners. Our services primarily include daily cleaning, floor care, window cleaning, and carpet cleaning.

Our company holds certificates for ISO 9001, ISO 14001, ISO 45001 and "Hjorten".

Referring to "the Swedish model" we honor collective agreements between Veltrio (employer-representative organisation and relevant labour unions (e.g. Arbetsfront).
The final design should communicate that we are a trustworthy company with a well trained staff, high quality services combined with a commitment to run a sustainable business from a labour and environmental perspective.

DETAILS
General
-----------------------------------------------
• Language: Swedish (we provide text)
• Very important: Easy to administrate for company staff without special technical skills, especially to
o add/change information about HQ staff
o change any text
o add/change information about offered services
• Responsive
• SEO-friendly

Content that web page needs to cover in one way or the other
--------------------------------------------
• Information about our company
• About our staff and contact info to HQstaff/management (photos, contact info)
• Our ambitions and supporting info (quality, environment, labour conditions, certificates, etc)
• Information to customers within the public sector
• Information to customers within the private sector
• Information to customers within the home owner sector
• Services public sector (Swedish = Offentlig sektor)
• Services private business sector (Swedish = Företag) Se törnvall
• Services home owner sector (Swedish=Privat)
• GDPR compliance
• News

Content/Function
-------------------------------
• One specific requirement is that we need a page for information to potentially new employees (some general information and open job positions) with a possibility to fill in a simple application form and upload CV.(Mail?) CAPTCHA or equivalent.
• Contact form for customers with CAPTCHA or equivalent.
• Cookie management
• Integration social media (future); easy to manage/add/delete integration of social media.

We are not interested in a blog at this point of time

```html
<!DOCTYPE html>
<html lang="en">
<head>
<meta charset="utf-8">
<title>TKR Clean AB – A Higher Standard of Clean</title>
<link href="https://fonts.googleapis.com/css2?family=Barlow:wght@400;500;600;700&display=swap" rel="stylesheet">
<style>
:root{
  --green:#4cb748;
  --green-dark:#3fa33b;
  --blue:#0a86d6;
  --blue-deep:#0b7fcc;
  --ink:#1e1e1e;
  --text:#333;
  --muted:#777;
  --line:#e3e3e3;
  --field:#f6f6f6;
  --white:#fff;
}
*{box-sizing:border-box;margin:0;padding:0}
html,body{width:1200px;height:3964px;overflow:hidden}
body{font-family:"Barlow",Arial,sans-serif;color:var(--ink);background:var(--white);position:relative}
a{color:inherit;text-decoration:none}
.abs{position:absolute}
svg.icon{display:inline-block;vertical-align:middle}

/* top bar */
.topbar{position:absolute;left:0;top:0;width:1200px;height:50px;border-bottom:1px solid var(--line)}
.social{position:absolute;display:flex;gap:12px}
.social span{width:13px;height:13px;border-radius:50%;background:var(--ink);display:block}
.topbar .social{left:86px;top:21px}
.topbar .contact{position:absolute;right:72px;top:17px;display:flex;gap:22px;font-size:11px;color:#444}
.topbar .contact span{display:flex;align-items:center;gap:5px}

/* header */
.header{position:absolute;top:50px;left:0;width:1200px;height:88px}
.brand{position:absolute;display:flex;align-items:center;gap:6px;font-size:30px;font-weight:500;color:var(--ink);letter-spacing:-.5px}
.brand i{width:14px;height:14px;background:var(--green);border-radius:50%;display:block}
.header .brand{left:84px;top:27px}
.nav{position:absolute;left:426px;top:36px;display:flex;gap:24px;font-size:12px;font-weight:500}
.btn-quote{position:absolute;right:70px;top:22px;width:128px;height:37px;background:var(--blue);color:#fff;font-size:12px;font-weight:600;display:flex;align-items:center;justify-content:center;letter-spacing:.3px}

/* hero */
.hero{position:absolute;top:138px;left:0;width:1200px;height:492px;overflow:hidden;
  background:linear-gradient(100deg,#c9d9c2 0%,#e8ece6 45%,#f4f5f2 70%,#dfe5e8 100%)}
.hero-tint{position:absolute;inset:0;background:linear-gradient(90deg,var(--green) 0%,rgba(76,183,72,.92) 32%,rgba(76,183,72,.35) 55%,rgba(76,183,72,0) 72%)}
.hero h1{position:absolute;left:118px;top:84px;font-size:43px;line-height:48px;font-weight:700;color:#fff}
.hero .lead{position:absolute;left:118px;top:186px;width:420px;font-size:27px;line-height:32px;color:#fff}
.btn-phone{position:absolute;width:166px;height:46px;background:#fff;color:var(--green);font-size:14px;font-weight:600;display:flex;align-items:center;justify-content:center;gap:12px}
.hero .btn-phone{left:114px;top:328px}
.hero-curve{position:absolute;left:0;bottom:0}

/* quote form */
.quote{position:absolute;left:697px;top:323px;width:385px;height:752px;background:#fff;border:1px solid #e6e6e6;border-radius:6px;box-shadow:0 2px 10px rgba(0,0,0,.05);z-index:3}
.quote h2{position:absolute;left:0;top:40px;width:100%;text-align:center;font-size:21px;font-weight:600}
.quote .sub{position:absolute;left:30px;top:72px;width:325px;text-align:center;font-size:13px;line-height:15px;color:#222}
.quote label{position:absolute;left:38px;font-size:12px;color:#222}
.quote label b{color:#e23;font-weight:400}
.field{position:absolute;left:38px;width:312px;height:48px;background:var(--field);border:1px solid #e2e2e2;font-size:11px;color:#999;padding:0 12px;display:flex;align-items:center;justify-content:space-between}
.check{position:absolute;left:38px;display:flex;align-items:flex-start;gap:10px;font-size:11px;color:#333}
.check i{width:20px;height:20px;border:1px solid #999;display:block;flex:none;background:#fff}
.captcha-mark{position:absolute;left:152px;top:538px;width:18px;height:18px;border-radius:4px;background:linear-gradient(135deg,#4a8ef0,#9cc0f6)}
.quote .terms{position:absolute;left:38px;top:620px;font-size:10.5px;color:#333}
.quote .terms a{color:var(--green);text-decoration:underline}
.btn-send{position:absolute;left:38px;top:655px;width:154px;height:37px;background:var(--blue);color:#fff;font-size:12px;font-weight:600;display:flex;align-items:center;justify-content:center}

/* results */
.results h2{position:absolute;left:114px;top:686px;font-size:32px;line-height:43px;font-weight:500}
.results p{position:absolute;left:114px;top:790px;width:450px;font-size:13.5px;line-height:21px;color:#222}
.benefits{position:absolute;left:114px;top:880px;width:420px;list-style:none}
.benefits li{position:relative;padding-left:30px;font-size:12px;line-height:19px;color:#222;margin-bottom:14px}
.benefits li svg{position:absolute;left:0;top:2px}

.badges{position:absolute;top:1138px;left:0;width:1200px;height:95px}
.badge{position:absolute;background:#dfe4ee}

/* services */
.services{position:absolute;top:1277px;left:0;width:1200px;height:603px;background:linear-gradient(180deg,#fff 0%,#e8f3fb 30%,#cfe5f6 100%)}
.services h2{position:absolute;top:58px;width:100%;text-align:center;font-size:32px;font-weight:500}
.svc{position:absolute;top:126px;width:310px;height:412px}
.svc .ph{position:absolute;inset:0}
.svc h3{position:absolute;left:31px;color:#fff;font-size:26px;line-height:28px;font-weight:600}
.btn-learn{position:absolute;left:32px;top:324px;width:117px;height:36px;background:var(--blue);color:#fff;font-size:11.5px;font-weight:600;display:flex;align-items:center;justify-content:center}

/* about */
.about{position:absolute;top:1880px;left:0;width:1200px;height:415px;
  background:linear-gradient(90deg,#6c6f72 0%,#8b8e8f 35%,#9c9d9c 60%,#6e7377 100%)}
.about::after{content:"";position:absolute;inset:0;background:rgba(40,45,55,.35)}
.about .inner{position:absolute;inset:0;z-index:2;color:#fff;text-align:center}
.eyebrow{font-size:15px;font-weight:600;letter-spacing:.5px}
.about .eyebrow{position:absolute;top:62px;width:100%}
.about h2{position:absolute;top:98px;width:100%;font-size:32px;font-weight:500}
.about p{position:absolute;left:230px;top:156px;width:740px;font-size:14px;line-height:21.5px}
.btn-more{position:absolute;left:532px;top:270px;width:140px;height:36px;background:var(--blue);color:#fff;font-size:11.5px;font-weight:600;display:flex;align-items:center;justify-content:center}

/* testimonials */
.testimonials{position:absolute;top:2295px;left:0;width:1200px;height:438px;background:var(--blue-deep);color:#fff;text-align:center}
.testimonials .eyebrow{position:absolute;top:62px;width:100%}
.testimonials h2{position:absolute;top:92px;width:100%;font-size:29px;font-weight:500}
.quote-card{position:absolute;top:146px;width:398px;height:223px;background:#fff;border-bottom:6px solid var(--green);text-align:left;color:#222}
.quote-card p{position:absolute;left:50px;top:52px;width:300px;font-size:12.5px;line-height:15.5px}
.person{position:absolute;left:50px;top:140px;display:flex;align-items:center;gap:12px;font-size:12px;line-height:15px}
.person i{width:32px;height:32px;border-radius:50%;background:linear-gradient(135deg,#8a8a8a,#c9c9c9);display:block}
.person b{font-weight:600}

/* environment */
.env-photo{position:absolute;left:118px;top:2819px;width:401px;height:333px;background:linear-gradient(135deg,#9fb4c8 0%,#dfe3e6 40%,#f3f3f3 65%,#b8bcc0 100%)}
.env h2{position:absolute;left:577px;top:2822px;font-size:29px;font-weight:500;color:var(--green)}
.env p{position:absolute;left:577px;top:2872px;width:510px;font-size:19px;line-height:24.5px;color:#222}
.env ul{position:absolute;left:579px;top:3015px;list-style:none}
.env li{display:flex;align-items:center;gap:16px;font-size:19px;line-height:35px;color:#222}

/* cta */
.cta{position:absolute;top:3242px;left:0;width:1200px;height:431px}
.cta .panel{position:absolute;left:0;top:0;width:617px;height:431px;background:var(--green);color:#fff}
.cta .photo{position:absolute;left:617px;top:0;width:583px;height:431px;background:linear-gradient(120deg,#e9eae7 0%,#d4d6d2 40%,#a9aca6 70%,#6c6f6a 100%)}
.cta h2{position:absolute;left:116px;top:97px;font-size:29px;font-weight:500}
.cta p{position:absolute;left:114px;top:162px;font-size:19px;line-height:24px}
.cta .btn-phone{left:114px;top:237px}

/* footer */
.footer{position:absolute;top:3673px;left:0;width:1200px;height:291px;background:#f4f4f4}
.footer .brand{left:120px;top:48px}
.footer .social{left:118px;top:118px;gap:18px}
.footer .social span{width:16px;height:16px}
.footer h4{position:absolute;left:507px;top:55px;font-size:17px;font-weight:500}
.footer .info{position:absolute;left:511px;top:93px;font-size:11px;line-height:23px;color:#222}
.footer .info div{display:flex;align-items:center;gap:5px}
.footer .links{position:absolute;left:752px;top:44px;list-style:none;font-size:12px;line-height:21px;color:#222}
.footer .rule{position:absolute;left:135px;top:220px;width:930px;height:1px;background:#d8d8d8}
.footer .copy{position:absolute;top:246px;width:100%;text-align:center;font-size:11px;color:#222}
</style>
</head>
<body>

<div class="topbar">
  <div class="social" aria-label="Social media"><span></span><span></span><span></span><span></span></div>
  <div class="contact">
    <span><svg class="icon" width="12" height="12" viewBox="0 0 24 24" fill="none" stroke="#333" stroke-width="2"><path d="M12 22s7-7 7-12a7 7 0 0 0-14 0c0 5 7 12 7 12z"/><circle cx="12" cy="10" r="2.5"/></svg>Your address here</span>
    <span><svg class="icon" width="12" height="12" viewBox="0 0 24 24" fill="none" stroke="#333" stroke-width="2"><path d="M5 3h4l2 5-3 2a12 12 0 0 0 6 6l2-3 5 2v4a2 2 0 0 1-2 2A18 18 0 0 1 3 5a2 2 0 0 1 2-2z"/></svg>000-000-00</span>
    <span><svg class="icon" width="12" height="12" viewBox="0 0 24 24" fill="none" stroke="#333" stroke-width="2"><rect x="3" y="5" width="18" height="14"/><path d="M3 6l9 7 9-7"/></svg>info@website.com</span>
  </div>
</div>

<header class="header">
  <div class="brand"><i></i>TKR Clean AB</div>
  <nav class="nav">
    <a>Home</a><a>About us ⌄</a><a>Our Service</a><a>Employee ⌄</a><a>Case management</a><a>Contact us ⌄</a><a>News</a>
  </nav>
  <a class="btn-quote">GET A Q UOTE</a>
</header>

<section class="hero">
  <div class="abs" style="inset:0" role="img" aria-label="Cleaner wiping a window with a squeegee"></div>
  <div class="hero-tint"></div>
  <h1>A Higher Standard<br>of Clean</h1>
  <p class="lead">Delivering Expert Cleaning &amp; Disinfectionfor Your Facility and Everyone in It</p>
  <a class="btn-phone"><svg class="icon" width="15" height="15" viewBox="0 0 24 24" fill="none" stroke="#4cb748" stroke-width="2"><path d="M5 3h4l2 5-3 2a12 12 0 0 0 6 6l2-3 5 2v4a2 2 0 0 1-2 2A18 18 0 0 1 3 5a2 2 0 0 1 2-2z"/></svg>08-512 30 40</a>
  <svg class="hero-curve" width="1200" height="492" viewBox="0 0 1200 492">
    <path d="M0 470 C260 425 640 468 1200 372 L1200 492 L0 492Z" fill="#fff"/>
    <path d="M0 466 C260 421 640 464 1200 368" fill="none" stroke="#0a86d6" stroke-width="4"/>
    <path d="M1080 386 C1130 374 1170 366 1200 358 L1200 380 C1170 388 1130 396 1080 404Z" fill="#0a86d6"/>
  </svg>
</section>

<form class="quote">
  <h2>Get Your Personalized Quote</h2>
  <p class="sub">Complete the form below and a member of our team will reach out to create your custom quote.</p>
  <label style="top:151px">Your name<b>*</b></label>
  <div class="field" style="top:172px">type your name</div>
  <label style="top:236px">Email<b>*</b></label>
  <div class="field" style="top:260px">type your last name</div>
  <label style="top:322px">Choose a service <b>*</b></label>
  <div class="field" style="top:348px">Public sector <span>⌄</span></div>
  <label style="top:421px">How can we help? <b>*</b></label>
  <div class="field" style="top:448px;height:65px"></div>
  <div class="check" style="top:538px"><i></i><span style="padding-top:3px">i'm not robot</span></div>
  <span class="captcha-mark" role="img" aria-label="Captcha check"></span>
  <div class="check" style="top:580px"><i></i><span style="line-height:14px">I understand that the the information provided by me<br>issubject to the privacy policy</span></div>
  <p class="terms">by sumbitting this form. you agree to the <a>terms</a> and <a>privacy policy</a></p>
  <a class="btn-send">SEND MY REQUEST</a>
</form>

<section class="results">
  <h2>Get Results With A Top-Rated<br>Cleaning Company</h2>
  <p>The cleanliness of your facilities directly impacts the people who use them every day. Our personalized custom service, flexible scheduling, and safe and effective cleaning products deliver unmatched results.</p>
  <ul class="benefits">
    <li><svg width="17" height="17" viewBox="0 0 24 24" fill="none" stroke="#111" stroke-width="2"><circle cx="12" cy="12" r="10"/><path d="M7 12l3.5 3.5L17 9"/></svg><b>Flexible:</b> Determine a flexible schedule and service agreement that accommodates your day-to-day operations.</li>
    <li><svg width="17" height="17" viewBox="0 0 24 24" fill="none" stroke="#111" stroke-width="2"><circle cx="12" cy="12" r="10"/><path d="M7 12l3.5 3.5L17 9"/></svg><b>Certified &amp; Professionally Trained:</b> Trust our professionally trained technicians, who undergo extensive background checks and use the latest tools and methods.</li>
    <li><svg width="17" height="17" viewBox="0 0 24 24" fill="none" stroke="#111" stroke-width="2"><circle cx="12" cy="12" r="10"/><path d="M7 12l3.5 3.5L17 9"/></svg><b>Responsive:</b> Call in to our main line to talk to a person and get an answer right away. No call centers, no complications.</li>
  </ul>
</section>

<div class="badges" aria-label="Certificates">
  <div class="badge" style="left:215px;top:12px;width:168px;height:64px;border-radius:6px;background:#d9dcef" role="img" aria-label="Quality certificate"></div>
  <div class="badge" style="left:487px;top:10px;width:110px;height:66px;border-radius:4px;background:#d3ecd2" role="img" aria-label="Environmental certificate"></div>
  <div class="badge" style="left:688px;top:4px;width:85px;height:85px;border-radius:50%;background:#d6e2f2" role="img" aria-label="Standards certificate"></div>
  <div class="badge" style="left:851px;top:0;width:98px;height:98px;border-radius:50%;background:#d3ecd2" role="img" aria-label="Eco label"></div>
</div>

<section class="services">
  <h2>Our Services</h2>
  <article class="svc" style="left:114px">
    <div class="ph" role="img" aria-label="Cleaner wiping a window in a public building" style="background:linear-gradient(160deg,#e9ecea 0%,#c3c7c6 55%,#7d8282 100%)"></div>
    <h3 style="top:289px">Public Sector</h3><a class="btn-learn">LEARN MORE</a>
  </article>
  <article class="svc" style="left:440px">
    <div class="ph" role="img" aria-label="Cleaning team in an office" style="background:linear-gradient(160deg,#eef0f1 0%,#c9cdd0 55%,#878c90 100%)"></div>
    <h3 style="left:49px;top:289px">Private Sector</h3><a class="btn-learn">LEARN MORE</a>
  </article>
  <article class="svc" style="left:767px">
    <div class="ph" role="img" aria-label="Cleaners vacuuming a home" style="background:linear-gradient(160deg,#eae7e2 0%,#c8c4bd 55%,#7f7d78 100%)"></div>
    <h3 style="left:46px;top:260px">Home Owner<br>Sector</h3><a class="btn-learn" style="left:48px">LEARN MORE</a>
  </article>
</section>

<section class="about" role="img" aria-label="Smiling cleaning team with mops and gloves">
  <div class="inner">
    <div class="eyebrow">ABOUT US</div>
    <h2>We Are Your DEDICATED Cleaning Support Team</h2>
    <p>Lorem ipsum dolor sit amet consectetur. Amet volutpat cursus nec non at at lectus sapien placerat. Malesuada sit massa cum eleifend a molestie elementum sed. Commodo at in tempus commodo. Risus interdum dignissim porttitor eu amet. Justo sit amet tortor cras nisl tincidunt. Tincidunt eu eros luctus lectus venenatis facilisis ac. Urna semper fringilla urna metus dignissim et suscipit velit at.</p>
    <a class="btn-more">MORE ABOUT US</a>
  </div>
</section>

<section class="testimonials">
  <div class="eyebrow">TESTIMONIAL</div>
  <h2>Testimonial</h2>
  <div class="quote-card" style="left:194px">
    <p>Lorem ipsum dolor sit amet consectetur. Tellus nam vulputate pulvinar malesuada adipiscing sed. Sem natoque sit pretium accumsan integer. Dictumst in molestie in nulla et vitae iaculis.</p>
    <div class="person"><i role="img" aria-label="Portrait"></i><div><b>John Doe</b><br>Employee at Norrvik</div></div>
  </div>
  <div class="quote-card" style="left:626px">
    <p>Lorem ipsum dolor sit amet consectetur. Tellus nam vulputate pulvinar malesuada adipiscing sed. Sem natoque sit pretium accumsan integer. Dictumst in molestie in nulla et vitae iaculis.</p>
    <div class="person"><i role="img" aria-label="Portrait"></i><div><b>John Doe</b><br>Employee at Norrvik</div></div>
  </div>
</section>

<section class="env">
  <div class="env-photo" role="img" aria-label="Gloved hand spraying and wiping an office desk"></div>
  <h2>We Think About The Environment</h2>
  <p>TKR Clean AB strives forenvironmentally friendly cleaning, andwith the right cleaning equipment,chemicals are rarely needed. But in cases whereit is necessary, we choose eco-labelled goods.</p>
  <ul>
    <li><svg width="17" height="17" viewBox="0 0 24 24" fill="none" stroke="#111" stroke-width="2"><circle cx="12" cy="12" r="10"/><path d="M7 12l3.5 3.5L17 9"/></svg>Eco-friendly products</li>
    <li><svg width="17" height="17" viewBox="0 0 24 24" fill="none" stroke="#111" stroke-width="2"><circle cx="12" cy="12" r="10"/><path d="M7 12l3.5 3.5L17 9"/></svg>Allergy-reducing equipment</li>
    <li><svg width="17" height="17" viewBox="0 0 24 24" fill="none" stroke="#111" stroke-width="2"><circle cx="12" cy="12" r="10"/><path d="M7 12l3.5 3.5L17 9"/></svg>CDC-recommended disinfectants</li>
  </ul>
</section>

<section class="cta">
  <div class="panel">
    <h2>Expect A Different Kind Of Clean</h2>
    <p>Choose a cleaning company dedicated<br>to leaving your facility spotless.</p>
    <a class="btn-phone"><svg class="icon" width="15" height="15" viewBox="0 0 24 24" fill="none" stroke="#4cb748" stroke-width="2"><path d="M5 3h4l2 5-3 2a12 12 0 0 0 6 6l2-3 5 2v4a2 2 0 0 1-2 2A18 18 0 0 1 3 5a2 2 0 0 1 2-2z"/></svg>08-512 30 40</a>
  </div>
  <div class="photo" role="img" aria-label="Cleaners vacuuming and tidying an office"></div>
</section>

<footer class="footer">
  <div class="brand"><i></i>TKR Clean AB</div>
  <div class="social" aria-label="Social media"><span></span><span></span><span></span><span></span></div>
  <h4>Contact Us</h4>
  <div class="info">
    <div><svg class="icon" width="12" height="12" viewBox="0 0 24 24" fill="none" stroke="#222" stroke-width="2"><path d="M12 22s7-7 7-12a7 7 0 0 0-14 0c0 5 7 12 7 12z"/><circle cx="12" cy="10" r="2.5"/></svg>Your address here</div>
    <div><svg class="icon" width="12" height="12" viewBox="0 0 24 24" fill="none" stroke="#222" stroke-width="2"><path d="M5 3h4l2 5-3 2a12 12 0 0 0 6 6l2-3 5 2v4a2 2 0 0 1-2 2A18 18 0 0 1 3 5a2 2 0 0 1 2-2z"/></svg>000-000-00</div>
    <div><svg class="icon" width="12" height="12" viewBox="0 0 24 24" fill="none" stroke="#222" stroke-width="2"><rect x="3" y="5" width="18" height="14"/><path d="M3 6l9 7 9-7"/></svg>info@website.com</div>
  </div>
  <ul class="links">
    <li>Home</li><li>About us ⌄</li><li>Our Service</li><li>Employee ⌄</li><li>Case management</li><li>Contact us ⌄</li><li>News</li>
  </ul>
  <div class="rule"></div>
  <div class="copy">©2022 TKR Clean AB</div>
</footer>

</body>
</html>
```